Harbinger Slabworks, Inc. Business Card

Create a business card that is eye catching and based around concrete sawcutting. I've attached our current business card and logo for reference. We like aspects of the current business card, but it is starting to feel very loud and lost. We would like something that is still fun but is more modern and streamlined.

```html
<!DOCTYPE html>
<html lang="en">
<head>
<meta charset="utf-8">
<title>Harbinger Slabworks, Inc. Business Card</title>
<link href="https://fonts.googleapis.com/css2?family=Montserrat:wght@400;500;600&family=Oswald:wght@500&display=swap" rel="stylesheet">
<style>
  :root {
    --page: #3a3a3c;
    --card-dark: #0d0d0e;
    --card-mid: #222225;
    --white: #f2f2f2;
    --grey: #c9c9c9;
    --red: #e01b24;
    --flag-red: #5a1b22;
    --flag-blue: #23294a;
  }
  html, body {
    margin: 0; padding: 0;
    width: 1200px; height: 1200px;
    overflow: hidden;
    background: var(--page);
  }
  .canvas {
    position: relative;
    width: 1200px; height: 1200px;
    display: flex; flex-direction: column;
    align-items: center; justify-content: center;
    gap: 36px;
  }
  .card {
    position: relative;
    width: 960px; height: 548px;
    border-radius: 30px;
    overflow: hidden;
    box-shadow: 0 18px 40px rgba(0,0,0,.55);
    font-family: "Montserrat", sans-serif;
    color: var(--white);
  }
  .plate-texture {
    position: absolute; inset: 0;
    background: radial-gradient(ellipse at 60% 35%, var(--card-mid) 0%, var(--card-dark) 75%);
  }
  .flag-wave {
    position: absolute; left: 0; top: 0;
    width: 460px; height: 360px;
    background: linear-gradient(160deg, rgba(90,27,34,.0) 20%, rgba(90,27,34,.55) 50%, rgba(35,41,74,.65) 80%);
    -webkit-mask-image: linear-gradient(to right, #000 40%, transparent);
            mask-image: linear-gradient(to right, #000 40%, transparent);
  }
  .brand-mark {
    position: absolute;
    display: flex; align-items: center; gap: 18px;
    font-weight: 600; color: var(--white);
    letter-spacing: .04em; text-transform: uppercase;
  }
  .brand-mark .dot {
    flex: none; border-radius: 50%;
    background: var(--red);
  }
  .front .brand-mark { right: 70px; top: 120px; font-size: 34px; line-height: 1.15; }
  .front .brand-mark .dot { width: 34px; height: 34px; }
  .contact-block { position: absolute; left: 110px; top: 250px; }
  .person-name { font-size: 40px; font-weight: 600; letter-spacing: .02em; text-transform: uppercase; margin: 0; }
  .person-title { font-size: 22px; font-weight: 400; color: var(--grey); text-transform: uppercase; margin: 2px 0 24px; }
  .contact-list { list-style: none; margin: 0; padding: 0; font-size: 22px; }
  .contact-list li { display: flex; align-items: flex-start; gap: 16px; margin-bottom: 10px; }
  .contact-list svg { flex: none; width: 22px; height: 22px; margin-top: 3px; fill: var(--red); }
  .back .brand-mark {
    left: 50%; top: 150px; transform: translateX(-50%);
    font-size: 48px; white-space: nowrap;
  }
  .back .brand-mark .dot { width: 44px; height: 44px; }
  .hotline {
    position: absolute; left: 0; right: 0; top: 330px;
    display: flex; justify-content: center; align-items: center; gap: 14px;
    font-family: "Oswald", sans-serif; font-size: 46px; letter-spacing: .02em;
  }
  .hotline svg { width: 38px; height: 38px; fill: var(--red); }
  .service-list {
    position: absolute; left: 0; right: 0; bottom: 52px;
    list-style: none; margin: 0; padding: 0;
    display: flex; justify-content: center; align-items: center; gap: 22px;
    font-family: "Oswald", sans-serif; font-size: 26px; text-transform: uppercase;
    color: var(--grey);
  }
  .service-list .sep { width: 12px; height: 12px; border-radius: 50%; background: var(--red); }
</style>
</head>
<body>
<main class="canvas">

  <section class="card front" aria-label="Card front">
    <div class="plate-texture" role="img" aria-label="Black diamond-plate steel texture"></div>
    <div class="flag-wave" role="img" aria-label="Faint waving American flag"></div>
    <div class="brand-mark"><span class="dot"></span><span>Harbinger<br>Slabworks</span></div>
    <div class="contact-block">
      <h1 class="person-name">Dana Whitfield</h1>
      <p class="person-title">Owner</p>
      <ul class="contact-list">
        <li><svg viewBox="0 0 24 24"><path d="M6.6 10.8a15 15 0 006.6 6.6l2.2-2.2c.3-.3.7-.4 1-.2 1.1.4 2.3.6 3.6.6.6 0 1 .4 1 1V20c0 .6-.4 1-1 1A17 17 0 013 4c0-.6.4-1 1-1h3.5c.6 0 1 .4 1 1 0 1.3.2 2.5.6 3.6.1.3 0 .7-.2 1z"/></svg>855.410.2276</li>
        <li><svg viewBox="0 0 24 24"><path d="M7 1h10a2 2 0 012 2v18a2 2 0 01-2 2H7a2 2 0 01-2-2V3a2 2 0 012-2zm0 3v14h10V4zm5 15.5a1 1 0 100 2 1 1 0 000-2z"/></svg>973.555.0148</li>
        <li><svg viewBox="0 0 24 24"><path d="M2 5h20v14H2zm2 2v.5l8 5 8-5V7l-8 5z"/></svg>dana@harbingerslabworks.com</li>
        <li><svg viewBox="0 0 24 24"><path d="M12 2a7 7 0 017 7c0 5-7 13-7 13S5 14 5 9a7 7 0 017-7zm0 4a3 3 0 100 6 3 3 0 000-6z"/></svg>48 Millbrook Ave.<br>Ridgefield, NJ 07657</li>
      </ul>
    </div>
  </section>

  <section class="card back" aria-label="Card back">
    <div class="plate-texture" role="img" aria-label="Black diamond-plate steel texture"></div>
    <div class="brand-mark"><span class="dot"></span><span>Harbinger Slabworks</span></div>
    <div class="hotline">
      <svg viewBox="0 0 24 24"><path d="M6.6 10.8a15 15 0 006.6 6.6l2.2-2.2c.3-.3.7-.4 1-.2 1.1.4 2.3.6 3.6.6.6 0 1 .4 1 1V20c0 .6-.4 1-1 1A17 17 0 013 4c0-.6.4-1 1-1h3.5c.6 0 1 .4 1 1 0 1.3.2 2.5.6 3.6.1.3 0 .7-.2 1z"/></svg>
      <span>855-CUT-SLAB</span>
    </div>
    <ul class="service-list">
      <li>Wall Sawing</li><li class="sep"></li>
      <li>Core Drilling</li><li class="sep"></li>
      <li>Slab Sawing</li><li class="sep"></li>
      <li>Breaking &amp; Removal</li>
    </ul>
  </section>

</main>
</body>
</html>
```